Brightpath Dental Studio

Please go to www.brightpathdentalstudio.example and obtain the current company logo.
Doctors name are
Marita Velbonne, DDS
Denis Kalb, DMD
Addresses are
318 Larchmont Ave
Hollis Glen, NJ 07490
201-555-0147
And
872 14th St.
East Marrow, NJ 07218
201-555-0182
Theme of the business card should feel modrrn and similar to the website.
Front side should include company logo, doctors name, addresses, phone numbers.
Back of the card should include blank lines for patient's name. Date and time for next scheduled appointment. And notice of 24-hr cancellation courtesy policy.
Dental

```html
<!DOCTYPE html>
<html lang="en">
<head>
<meta charset="utf-8">
<title>Brightpath Dental Studio – Business Card</title>
<link href="https://fonts.googleapis.com/css2?family=Merriweather:wght@300;400&display=swap" rel="stylesheet">
<style>
  :root {
    --navy: #253370;
    --navy-ink: #2a3a86;
    --ink: #2b2b2b;
    --paper: #ffffff;
    --stage: #e4e5e8;
    --icon-bg: #eef0f5;
  }
  * { margin: 0; padding: 0; box-sizing: border-box; }
  html, body { width: 1200px; height: 1200px; overflow: hidden; }
  body {
    background: var(--stage);
    font-family: "Merriweather", Georgia, serif;
    font-weight: 300;
    color: var(--ink);
    position: relative;
  }
  .card {
    position: absolute;
    left: 176px;
    width: 848px;
    height: 448px;
    background: var(--paper);
    overflow: hidden;
  }
  /* Front */
  .card--front { top: 108px; border: 18px solid var(--navy); }
  .card--front .inner { position: absolute; left: -18px; top: -18px; width: 848px; height: 448px; }
  .brand {
    position: absolute;
    left: 104px; top: 206px;
    display: flex; align-items: center; gap: 12px;
  }
  .brand__dot { width: 26px; height: 26px; border-radius: 50%; background: var(--navy); }
  .brand__name { font-size: 27px; font-weight: 400; color: var(--ink); letter-spacing: 0.3px; white-space: nowrap; }

  .info-heading {
    position: absolute; left: 600px; width: 150px;
    font-size: 18px; font-weight: 400; color: var(--navy-ink);
    border-bottom: 1.5px solid var(--navy-ink);
    line-height: 22px; height: 24px;
  }
  .info-icon {
    position: absolute; left: 705px; width: 40px; height: 40px;
    border-radius: 50%; background: var(--icon-bg);
    display: flex; align-items: center; justify-content: center;
  }
  .info-text { position: absolute; left: 609px; white-space: nowrap; }
  .info-text--doctors { font-size: 12px; line-height: 16px; font-weight: 400; }
  .info-text--small { font-size: 9.5px; line-height: 12px; font-weight: 400; }
  .info-text--phone { font-size: 9.5px; line-height: 14px; font-weight: 400; }

  /* Back */
  .card--back { top: 644px; }
  .back-panel { position: absolute; inset: 0; }
  .field-heading {
    position: absolute; font-size: 18px; font-weight: 400; color: var(--navy-ink);
  }
  .field {
    position: absolute; left: 0; width: 300px; height: 16px;
  }
  .field__label {
    position: absolute; right: 156px; bottom: 0;
    font-size: 12px; font-weight: 400; color: var(--ink);
  }
  .field__line {
    position: absolute; left: 150px; width: 149px; bottom: 2px;
    border-bottom: 1.5px solid var(--navy-ink);
  }
  .policy {
    position: absolute; left: 518px; width: 300px; top: 108px;
    text-align: center; color: #fff; white-space: nowrap;
    font-size: 16.5px; line-height: 26px; font-weight: 300;
  }
  .policy p + p { margin-top: 26px; }
</style>
</head>
<body>

<section class="card card--front" aria-label="Card front">
  <div class="inner">
    <div class="brand">
      <span class="brand__dot"></span>
      <span class="brand__name">Brightpath Dental Studio</span>
    </div>

    <div class="info-icon" style="top:80px">
      <svg width="20" height="22" viewBox="0 0 20 22"><circle cx="10" cy="6" r="5" fill="#253370"/><path d="M1 22 C1 14 19 14 19 22Z" fill="#253370"/></svg>
    </div>
    <h2 class="info-heading" style="top:90px">Doctors</h2>
    <p class="info-text info-text--doctors" style="top:123px">Marita Velbonne, DDS<br>Denis Kalb, DMD</p>

    <div class="info-icon" style="top:176px">
      <svg width="22" height="20" viewBox="0 0 22 20"><path d="M11 1 L21 10 H18 V19 H13 V13 H9 V19 H4 V10 H1Z" fill="#253370"/></svg>
    </div>
    <h2 class="info-heading" style="top:186px">Addresses</h2>
    <p class="info-text info-text--small" style="top:218px">318 Larchmont Ave<br>Hollis Glen, NJ 07490</p>
    <p class="info-text info-text--small" style="top:250px">872 14th St.<br>East Marrow, NJ 07218</p>

    <div class="info-icon" style="top:296px">
      <svg width="20" height="20" viewBox="0 0 20 20"><path d="M3 2 L7 2 L8 6 L6 7 L13 14 L14 12 L18 13 L18 17 L16 18 L2 4Z" fill="#253370" transform="rotate(-10 10 10)"/></svg>
    </div>
    <h2 class="info-heading" style="top:306px">Phone</h2>
    <p class="info-text info-text--phone" style="top:337px">201-555-0147<br>201-555-0182</p>
  </div>
</section>

<section class="card card--back" aria-label="Card back">
  <svg class="back-panel" width="848" height="448" viewBox="0 0 848 448" aria-hidden="true">
    <polygon points="542,0 848,0 848,448 0,448 0,428 362,428" fill="#253370"/>
  </svg>

  <h2 class="field-heading" style="left:80px; top:114px">Patient</h2>
  <div class="field" style="top:153px"><span class="field__label">Name</span><span class="field__line"></span></div>

  <h2 class="field-heading" style="left:62px; top:239px">Schedule</h2>
  <div class="field" style="top:279px"><span class="field__label">Date</span><span class="field__line"></span></div>
  <div class="field" style="top:308px"><span class="field__label">Time</span><span class="field__line"></span></div>

  <div class="policy">
    <p>If you need to cancel or<br>reschedule your appointment,<br>we kindly ask that you give<br>us a 24 hour notice so we<br>have time to schedule<br>another patient.</p>
    <p>Otherwise your<br>account may be charged.</p>
  </div>
</section>

</body>
</html>
```